integrative health clinic-Medical massage, acupuncture, chiropractic

we like our logo, but are open to new ideas. We need a new card design. We have added chiropractic and acupuncture that we have put under the name of the business. We are an integrative medical clinic

Target Market(s)

General public, athletes

Contact Information for Business Card

Phone 5055583927
Fax 5055583926
Hours Monday-Friday 9-6
Saturday 10-6
The 20% can be smaller on the back

Colors
3176b5
0355a3

Requirements
Must have
• Logo but am open to ideas
Nice to have
• We are an integrated medical clinic but also want to be personable. We want the card fun and inviting

```html
<!DOCTYPE html>
<html lang="en">
<head>
<meta charset="utf-8">
<title>Kinetic Harbor Wellness – Business Card</title>
<link href="https://fonts.googleapis.com/css2?family=Arimo:wght@400;700&family=Roboto+Condensed:wght@700&family=Pinyon+Script&display=swap" rel="stylesheet">
<style>
  :root{
    --royal:#2b3f9f;
    --royal-deep:#23368c;
    --accent:#3176b5;
    --brand:#0355a3;
    --ink:#1b1b1b;
    --paper:#ffffff;
    --stage:#2e2e2e;
    --line:rgba(255,255,255,.45);
  }
  *{box-sizing:border-box;margin:0;padding:0}
  html,body{width:1200px;height:866px;overflow:hidden}
  body{background:var(--stage);font-family:"Arimo",Arial,sans-serif;display:flex;align-items:center;justify-content:center;gap:40px}
  .card{width:540px;height:309px;position:relative;overflow:hidden;box-shadow:0 10px 24px rgba(0,0,0,.45)}

  /* front */
  .card--front{background:var(--paper);color:var(--ink)}
  .contact{position:absolute;left:30px;top:48px;font-size:15px;line-height:1.3}
  .contact__row{display:flex;align-items:flex-start;gap:6px}
  .contact__row svg{flex:none;margin-top:2px}
  .contact__group{margin-top:14px}
  .brand{position:absolute;left:250px;top:40px;width:270px}
  .brand__name{display:flex;align-items:center;gap:10px;font-family:"Roboto Condensed",sans-serif;font-weight:700;font-size:33px;line-height:1;color:var(--ink);letter-spacing:-.3px}
  .brand__dot{width:22px;height:22px;border-radius:50%;background:var(--brand);flex:none}
  .brand__tagline{margin:8px 0 0 32px;font-size:13px;color:var(--ink)}
  .brand__services{margin:4px 0 0 32px;font-size:9.5px;font-weight:700;letter-spacing:1.2px;color:var(--accent)}
  .hours{position:absolute;right:28px;top:168px;text-align:right;font-size:15px;line-height:1.3}
  .hours__title{color:var(--brand);font-size:15px;letter-spacing:.5px}
  .band{position:absolute;left:0;right:0;bottom:0;height:52px;background:var(--royal);color:#fff;font-size:15px;display:flex;align-items:center;padding-left:30px}

  /* back */
  .card--back{background:var(--royal);color:#fff;text-align:center}
  .card--back::before{content:"";position:absolute;inset:0;background:radial-gradient(circle at 50% 50%,var(--royal-deep) 0,transparent 60%);opacity:.7}
  .back__inner{position:relative;padding-top:42px}
  .back__book{font-size:14px}
  .back__url{font-family:"Pinyon Script",cursive;font-size:34px;margin-top:2px}
  .rule{height:1px;background:var(--line);margin:10px auto;width:300px}
  .back__offer{font-size:15px;letter-spacing:.5px}
  .divider{display:flex;align-items:center;justify-content:center;gap:12px;margin:12px 0}
  .divider span{width:110px;height:1px;background:var(--line)}
  .divider i{width:24px;height:24px;border:1.5px solid #fff;border-radius:50%;display:block}
  .back__note{font-size:14px;line-height:1.35}
</style>
</head>
<body>
  <section class="card card--front">
    <div class="contact">
      <div class="contact__row">
        <svg width="10" height="14" viewBox="0 0 10 14"><path d="M5 0a5 5 0 0 0-5 5c0 4 5 9 5 9s5-5 5-9a5 5 0 0 0-5-5zm0 7a2 2 0 1 1 0-4 2 2 0 0 1 0 4z" fill="#0355a3"/></svg>
        <div>1480 Alameda Row, B4<br>Mesa Verde, NM 87510</div>
      </div>
      <div class="contact__group">
        <div class="contact__row">
          <svg width="13" height="12" viewBox="0 0 13 12"><path d="M1 3c2-3 9-3 11 0l-2 2-2-1V3H5v1L3 5zM3 6h7l2 5H1z" fill="#1b1b1b"/></svg>
          <span>5055583927</span>
        </div>
        <div class="contact__row">
          <svg width="13" height="12" viewBox="0 0 13 12"><rect x="3" y="0" width="7" height="4" fill="#1b1b1b"/><rect x="0" y="4" width="13" height="6" rx="1" fill="#1b1b1b"/><rect x="3" y="8" width="7" height="4" fill="#fff" stroke="#1b1b1b"/></svg>
          <span>5055583926</span>
        </div>
        <div class="contact__row">
          <svg width="13" height="10" viewBox="0 0 13 10"><rect width="13" height="10" fill="#1b1b1b"/><path d="M0 0l6.5 5L13 0" stroke="#fff" fill="none"/></svg>
          <span>info@kineticharbornm.com</span>
        </div>
      </div>
    </div>

    <div class="brand">
      <div class="brand__name"><span class="brand__dot"></span>Kinetic Harbor Wellness</div>
      <div class="brand__tagline">Sports Therapy and Wellness Center</div>
      <div class="brand__services">CHIROPRACTIC AND ACUPUNCTURE</div>
    </div>

    <div class="hours">
      <div class="hours__title">HOURS</div>
      <div>Monday-Friday 9 AM-6 PM</div>
      <div>Saturday 10 AM-6 PM</div>
    </div>

    <div class="band">Specializing in Medical, Sports Massage and Manual Therapies</div>
  </section>

  <section class="card card--back">
    <div class="back__inner">
      <div class="back__book">Book Online</div>
      <div class="back__url">www.kineticharbornm.com</div>
      <div class="rule"></div>
      <div class="back__offer">20% OFF FIRST VISIT</div>
      <div class="divider"><span></span><i></i><span></span></div>
      <div class="back__note">We Accept some insurances, Worker's<br>Comp and Personal Injury</div>
    </div>
  </section>
</body>
</html>
```